Letterhead design for Dental Practice - Ashby Lane Dental Care

Letterhead for Private Dental Practice. To be used for all official correspondance and for printing treatment details on to be given to patients.

Target Market(s)

Private dental patients

Industry/Entity Type

Dental Clinic

Font styles to use
Other font styles liked:
• nexa-light

Colors
33a6d7
1c66ac
85abd2

Requirements
Must have
• info in the footer and header needs to be 3.5cm from upper/lower boader of paper, see photo in uploaded files
• info details:
• tel. 0115 947 3051
• email info@ashbylanedc.co.uk
• ashbylanedentalcare.co.uk
• 17b Ashby Lane Eastmere Nottingham NG14 7QT
• nexa-light font as in uploaded logo files
Should not have
• No funny tooth pictures

```html
<!DOCTYPE html>
<html lang="en">
<head>
<meta charset="utf-8">
<title>Ashby Lane Dental Care – Letterhead</title>
<link rel="stylesheet" href="https://fonts.googleapis.com/css2?family=Quicksand:wght@400;500;600&display=swap">
<style>
  :root {
    --brand-blue: #33a6d7;
    --deep-blue: #1c66ac;
    --steel: #85abd2;
    --headline-grey: #858585;
    --body-grey: #555555;
    --footer-ink: #2b2b2b;
    --paper: #ffffff;
  }
  * { margin: 0; padding: 0; box-sizing: border-box; }
  html, body { width: 849px; height: 1200px; overflow: hidden; background: var(--paper); }
  .letterhead {
    position: relative; width: 849px; height: 1200px; overflow: hidden;
    background: var(--paper);
    font-family: "Quicksand", sans-serif;
  }
  .header-band, .footer-band { position: absolute; left: 0; width: 849px; display: block; }
  .header-band { top: 0; height: 150px; }
  .footer-band { bottom: 0; height: 40px; }

  .practice-name {
    position: absolute; left: 32px; top: 96px;
    color: var(--paper); font-size: 26px; font-weight: 500; line-height: 1;
  }

  .headline {
    position: absolute; left: 70px; top: 276px;
    color: var(--headline-grey); font-weight: 400;
    font-size: 64px; line-height: 74px; letter-spacing: 3px; text-transform: uppercase;
  }
  .headline span { display: block; }

  .letter-body {
    position: absolute; left: 74px; top: 446px; width: 682px;
    color: var(--body-grey); font-size: 16px; line-height: 22px; font-weight: 500;
    text-align: justify;
  }
  .letter-body p + p { margin-top: 4px; }

  .signature {
    position: absolute; left: 538px; top: 856px;
    color: var(--headline-grey); font-size: 20px; line-height: 34px; font-weight: 500;
    text-transform: uppercase;
  }

  .contact {
    position: absolute; top: 1121px; color: var(--footer-ink);
    font-size: 11.5px; line-height: 16px; font-weight: 600; text-align: right;
  }
  .contact-web { right: 252px; top: 1137px; }
  .contact-post { right: 26px; }
  .contact-divider {
    position: absolute; left: 616px; top: 1126px; width: 1px; height: 44px;
    background: var(--footer-ink);
  }
</style>
</head>
<body>
<main class="letterhead">
  <svg class="header-band" viewBox="0 0 849 150" aria-hidden="true">
    <defs>
      <linearGradient id="headerFill" x1="0" y1="0" x2="1" y2="0">
        <stop offset="0" stop-color="#1c66ac"/>
        <stop offset="1" stop-color="#33a6d7"/>
      </linearGradient>
    </defs>
    <path fill="url(#headerFill)" d="M0 0 H849 V78 L560 140 H0 Z"/>
    <path fill="var(--steel)" d="M578 146 L849 88 V100 L634 146 Z"/>
  </svg>

  <div class="practice-name">Ashby Lane Dental Care</div>

  <h1 class="headline"><span>Headline</span><span>Lorem Ipsum</span></h1>

  <section class="letter-body">
    <p>Lorem ipsum dolor sit amet, consectetuer adipiscing elit, sed diam nonummy nibh euismod tincidunt ut laoreet dolore magna aliquam erat volutpat. Ut wisi enim ad minim veniam, quis nostrud exerci tation ullamcorper suscipit lobortis nisl ut aliquip ex ea commodo consequat. Duis autem vel eum iriure dolor in hendrerit in vulputate velit esse molestie consequat, vel illum dolore eu feugiat nulla facilisis at vero eros et accumsan et iusto odio dignissim qui blandit praesent luptatum zzril delenit augue.</p>
    <p>Lorem ipsum dolor sit amet, consectetuer adipiscing elit, sed diam nonummy nibh euismod tincidunt ut laoreet dolore magna aliquam erat volutpat. Ut wisi enim ad minim veniam, quis nostrud exerci tation ullamcorper suscipit lobortis nisl ut aliquip ex ea commodo consequat. Duis autem vel eum iriure dolor in hendrerit in vulputate.</p>
    <p>Lorem ipsum dolor sit amet, consectetuer adipiscing elit, sed diam nonummy nibh euismod tincidunt ut laoreet dolore magna aliquam erat volutpat. Ut wisi enim ad minim veniam, quis nostrud exerci tation ullamcorper suscipit.</p>
  </section>

  <div class="signature">
    <div class="signature-role">General Manager</div>
    <div class="signature-name">John Doe</div>
  </div>

  <div class="contact contact-web">
    <div>info@ashbylanedc.co.uk</div>
    <div>ashbylanedentalcare.co.uk</div>
  </div>
  <div class="contact-divider"></div>
  <div class="contact contact-post">
    <div>0115 947 3051</div>
    <div>17b Ashby Lane</div>
    <div>Eastmere Nottingham NG14 7QT</div>
  </div>

  <svg class="footer-band" viewBox="0 0 849 40" aria-hidden="true">
    <rect fill="var(--steel)" x="0" y="8" width="849" height="3"/>
    <rect fill="var(--brand-blue)" x="0" y="18" width="849" height="22"/>
  </svg>
</main>
</body>
</html>
```